Delcourt Realty Business Cards

Design business card

Target Market(s)

High-End Buyer of Real Estate over $1 million dollars

Industry/Entity Type

Realtor

Contact Information for Business Card

Lena Delcourt R(S) LIC.# 41972
Cell 555 246-1938
Email Lena@Delcourt.example
Website IsleFreshHomes.example

Also Need Cards for:

Hank Delcourt R(B) LIC# 69418
C 555 613-7052
E Hank@Delcourt.example
W IsleFreshHomes.example

Colors

Designer to choose colors to be used in the design.

Requirements
Must have
• Address on back:
• 287 Pohaku Cir. , Kelowai HI 96799
• Logo on back
Nice to have
• I would like the phone numbers and email address to be big so people can read it easily
Should not have
• Very small print Except For: address (287 Pohaku Cir. Wailea HI 96753)

```html
<!DOCTYPE html>
<html lang="en">
<head>
<meta charset="utf-8">
<title>Delcourt Realty Business Cards</title>
<link href="https://fonts.googleapis.com/css2?family=Lato:wght@400;700;900&display=swap" rel="stylesheet">
<style>
  :root {
    --stage: #848484;
    --card-white: #ffffff;
    --ink: #0b0b0b;
    --dark-top: #666666;
    --dark-bottom: #000000;
    --mark-grey: #b4b4b4;
    --gold: #e7b42f;
    --text-light: #ffffff;
  }
  * { margin: 0; padding: 0; box-sizing: border-box; }
  html, body { width: 1200px; height: 1187px; overflow: hidden; }
  body { background: var(--stage); font-family: "Lato", sans-serif; position: relative; }

  .card { position: absolute; top: 298px; width: 322px; height: 578px; overflow: hidden; }

  .card-front { left: 65px; background: var(--card-white); border-top-right-radius: 40px; }
  .front-brand {
    position: absolute; left: 40px; top: 41px; width: 237px; height: 78px;
    background: var(--ink); border-radius: 10px;
    display: flex; align-items: center; justify-content: center;
    color: var(--text-light); font-weight: 700; font-size: 25px;
    letter-spacing: 3px; line-height: 1.15; text-align: center;
  }
  .front-photo {
    position: absolute; left: 0; top: 198px; width: 322px; height: 380px;
    background: linear-gradient(100deg, #f2e6de 0%, #d33a78 35%, #2a2a2a 60%, #111 100%);
  }

  .card-back {
    background: linear-gradient(to bottom, var(--dark-top) 0%, #2a2a2a 40%, var(--dark-bottom) 75%);
    border-top-left-radius: 52px; color: var(--text-light); text-align: center;
  }
  .card-back.agent-lena { left: 427px; }
  .card-back.agent-hank { left: 785px; }

  .back-brand {
    position: absolute; left: 122px; top: 62px; width: 85px; height: 141px;
    display: flex; flex-direction: column; align-items: center; justify-content: space-between;
    color: var(--mark-grey); font-weight: 700; font-size: 13px; letter-spacing: 2px;
  }
  .back-brand .brand-square { width: 66px; height: 66px; background: var(--mark-grey); border-radius: 4px; }

  .agent-name { position: absolute; left: 0; right: 0; top: 283px; font-size: 30px; font-weight: 400; }
  .agent-license { position: absolute; left: 0; right: 0; top: 322px; font-size: 29px; letter-spacing: 6px; }
  .divider {
    position: absolute; left: 37px; width: 248px; height: 7px;
    background: repeating-linear-gradient(115deg, var(--text-light) 0 7px, var(--dark-bottom) 7px 9px);
  }
  .divider.top { top: 366px; }
  .divider.bottom { top: 477px; }
  .agent-phone { position: absolute; left: 0; right: 0; top: 380px; font-size: 40px; font-weight: 900; color: var(--gold); }
  .agent-email { position: absolute; left: 0; right: 0; top: 436px; font-size: 22px; font-weight: 900; color: var(--gold); }
  .agent-site { position: absolute; left: 0; right: 0; top: 493px; font-size: 24px; }
  .office-address { position: absolute; left: 0; right: 0; top: 528px; font-size: 15px; }
</style>
</head>
<body>
  <section class="card card-front">
    <div class="front-brand">DELCOURT<br>REALTY</div>
    <div class="front-photo" role="img" aria-label="Portrait photo of Lena and Hank Delcourt"></div>
  </section>

  <section class="card card-back agent-lena">
    <div class="back-brand"><span>DELCOURT</span><span class="brand-square"></span><span>REALTY</span></div>
    <p class="agent-name">Lena Delcourt R(S)</p>
    <p class="agent-license">LIC# 41972</p>
    <div class="divider top"></div>
    <p class="agent-phone">555.246.1938</p>
    <p class="agent-email">Lena@Delcourt.example</p>
    <div class="divider bottom"></div>
    <p class="agent-site">IsleFreshHomes.example</p>
    <p class="office-address">287 Pohaku Cir. , Kelowai HI 96799</p>
  </section>

  <section class="card card-back agent-hank">
    <div class="back-brand"><span>DELCOURT</span><span class="brand-square"></span><span>REALTY</span></div>
    <p class="agent-name">Hank Delcourt R(B)</p>
    <p class="agent-license">LIC# 69418</p>
    <div class="divider top"></div>
    <p class="agent-phone">555.613.7052</p>
    <p class="agent-email">Hank@Delcourt.example</p>
    <div class="divider bottom"></div>
    <p class="agent-site">IsleFreshHomes.example</p>
    <p class="office-address">287 Pohaku Cir. , Kelowai HI 96799</p>
  </section>
</body>
</html>
```